Verpackungsdesign für CBD-Öl
Bin voll begeistert, viele meiner Änderungswünsche wurden umgesetzt, einfach super gelaufen. Klasse Arbeit. Kann JorisKeller nur weiterempfehlen. Vielen Dank
Zielgruppe
CBD Produkte
Aufgabenstellung
Erstellung eines Designs für eine Verpackung von CBD-Öl. Die Verpackung sollte sich von den üblichen CBD Verpackungen abheben, mit Logo,, Hintergrund und Farben meiner Webseite sollte gearbeitet werden siehe Foto.
Design sollte sehr edel und cool ausschauen, nicht wie die meisten CBD Verpackungen. Eure Kreativität könnt Ihr freien Lauf lassen. Wir lassen uns überraschen.
Größe der Faltschachtel: Länge 27 mm, Breite 28 mm, Höhe 90 mm
Erstellung eines Design für eine Faltschachtel mit 4 verschiedenen Inhaltsangaben.
Das Grunddesign der Verpackung ist immer das gleiche, nur die Inhaltsangabe an Cannabidiol variiert.
10 % 1000MG, 15 % 1500MG, 20 % 2000MG, 30 % 3000MG
Torvelin sollte im Vordergrund stehen und der Hintergrund siehe Bild!
Was draufstehen sollte
Vegan & Glutenfrei
Vollspektrum
CBD Premium Hanföl
Nicht zum Verzehr geeignet
Duftöl
Siehe Bild von Vexa, die Inhaltsstoffe bitte freihalten, da wir unterschiedliche Inhaltsstoffe/ Geschmacksrichtungen haben.
Erstellung Design für das Etikett für die 10-ml-Flasche.
Größe Etikett: Länge: 85 mm, Höhe: 30 mm
Das Grunddesign für das Label der 10-ml-Flasche ist immer das gleiche. Jedoch auch hier variiert die Inhaltsangabe von Cannabidiol.
10% 15% 20% und 30%
Auch unser Firmenlogo TORVELIN können wir Ihnen in anderen Größen senden.
Sie können uns auch schreiben, um weitere Fragen abzuklären.
Gutes designen.

```html
<!DOCTYPE html>
<html lang="de">
<head>
<meta charset="utf-8">
<title>Torvelin CBD Hanföl – Faltschachtel</title>
<link rel="stylesheet" href="https://fonts.googleapis.com/css2?family=Fira+Sans+Extra+Condensed:wght@300;400&family=Montserrat:wght@500;600;700&display=swap">
<style>
  :root {
    --stage: #1e271f;
    --carton: #3a3a3a;
    --green: #5a9a3c;
    --green-box: #557f3a;
    --cream: #efe6c4;
    --gold: #d8c07a;
    --gold-deep: #a88a3c;
    --text: #f1f1ec;
    --badge: #8cc63f;
  }
  * { margin: 0; padding: 0; box-sizing: border-box; }
  html, body { width: 1200px; height: 800px; overflow: hidden; background: var(--stage); }
  .canvas { position: relative; width: 1200px; height: 800px; font-family: "Fira Sans Extra Condensed", sans-serif; color: var(--text); }

  .dieline { position: absolute; left: 305px; top: 20px; width: 591px; height: 760px; }
  .flap, .band { position: absolute; background: var(--carton); }
  .flap--top { left: 295px; top: 0; width: 150px; height: 148px; }
  .flap--bottom { left: 295px; top: 640px; width: 150px; height: 120px; }
  .band { left: 0; top: 148px; width: 591px; height: 492px; }
  .panel { position: absolute; top: 0; height: 492px; }
  .panel--side { left: 0; width: 153px; }
  .panel--info { left: 153px; width: 142px; }
  .panel--front { left: 295px; width: 150px; }
  .panel--details { left: 445px; width: 146px; }

  .brand { position: absolute; left: 0; right: 0; display: flex; align-items: center; justify-content: center; gap: 6px; font-family: "Fira Sans Extra Condensed", sans-serif; font-weight: 400; font-size: 21px; letter-spacing: 1.5px; color: var(--cream); }
  .brand__dot { width: 8px; height: 8px; border-radius: 50%; background: var(--green); }

  .leaf-art { position: absolute; background: linear-gradient(180deg, var(--gold) 0%, var(--gold-deep) 100%); opacity: .9; border-radius: 4px; }

  .notice { position: absolute; left: 7px; top: 38px; width: 123px; height: 42px; background: var(--green-box); font-size: 14px; line-height: 1.3; padding: 3px 8px; color: var(--cream); font-weight: 300; }
  .directions { position: absolute; left: 15px; top: 109px; width: 118px; font-size: 9.5px; line-height: 1.5; font-weight: 300; }
  .directions p { margin-bottom: 14px; }

  .title { position: absolute; left: 10px; top: 116px; height: 277px; writing-mode: vertical-rl; transform: rotate(180deg); font-family: "Montserrat", sans-serif; font-weight: 600; font-size: 44px; line-height: 1; white-space: nowrap; }
  .title__cbd { color: var(--green); font-weight: 700; }
  .title__oil { color: var(--cream); font-weight: 500; }
  .variant { position: absolute; left: 63px; top: 298px; height: 95px; writing-mode: vertical-rl; transform: rotate(180deg); font-family: "Montserrat", sans-serif; font-weight: 700; font-size: 17px; color: var(--cream); }
  .strength { position: absolute; left: 79px; top: 188px; font-family: "Montserrat", sans-serif; font-weight: 700; font-size: 27px; color: var(--gold); }
  .claim { position: absolute; left: 81px; top: 222px; width: 66px; font-size: 13.5px; line-height: 1.4; font-weight: 300; }

  .features { position: absolute; left: 12px; top: 14px; list-style: none; }
  .features li { display: flex; align-items: center; gap: 8px; height: 30px; font-size: 11.5px; font-weight: 300; }
  .features svg { width: 24px; height: 24px; }
  .bio-badge { position: absolute; left: 15px; top: 109px; width: 74px; height: 40px; background: var(--badge); }
  .facts { position: absolute; left: 15px; top: 155px; list-style: none; font-size: 9.5px; line-height: 1.55; font-weight: 300; }
  .facts li::before { content: "• "; }
  .ingredients { position: absolute; left: 15px; top: 317px; font-size: 9.5px; line-height: 1.55; font-weight: 300; }

  .batch { position: absolute; left: 12px; top: 14px; font-size: 14px; line-height: 1.55; font-weight: 300; }
  .batch-field { position: absolute; left: 8px; top: 82px; width: 125px; height: 38px; background: #fff; }
  .volume { position: absolute; left: 460px; top: 660px; font-size: 13px; font-weight: 300; }
</style>
</head>
<body>
<main class="canvas">
  <section class="dieline" aria-label="Faltschachtel Torvelin CBD Hanföl, abgewickelt">
    <div class="flap flap--top">
      <div class="brand" style="top:62px"><span class="brand__dot"></span>TORVELIN</div>
    </div>

    <div class="band">
      <div class="panel panel--side">
        <div class="brand" style="top:50px"><span class="brand__dot"></span>TORVELIN</div>
        <div class="leaf-art" role="img" aria-label="Goldenes Hanfblatt, angeschnitten" style="left:0;top:208px;width:65px;height:112px"></div>
      </div>

      <div class="panel panel--info">
        <div class="notice">Dieses Produkt ist kein Arzneimittel.</div>
        <div class="directions">
          <p>Vor Anwendung gut schütteln. Trocken, kühl und lichtgeschützt lagern.</p>
          <p>Nicht verwenden während der Schwangerschaft und Stillzeit.</p>
          <p>Außerhalb der Reichweite von Kindern aufbewahren.</p>
          <p>Vorsicht bei Hanfallergie.</p>
          <p>Geöffnet mindestens<br>3 Monate haltbar.</p>
        </div>
      </div>

      <div class="panel panel--front">
        <div class="brand" style="top:48px"><span class="brand__dot"></span>TORVELIN</div>
        <div class="title"><span class="title__cbd">CBD</span> <span class="title__oil">Hanföl</span></div>
        <div class="variant">Premium</div>
        <div class="strength">10%</div>
        <p class="claim">Das volle Spektrum der Hanfpflanze.</p>
        <div class="leaf-art" role="img" aria-label="Goldenes Hanfblatt" style="left:20px;top:425px;width:108px;height:67px"></div>
      </div>

      <div class="panel panel--details">
        <ul class="features">
          <li><svg viewBox="0 0 24 24"><circle cx="12" cy="12" r="10.5" fill="none" stroke="var(--gold)" stroke-width="1.5"/><path d="M7 12.5l3.2 3.2L17 9" fill="none" stroke="var(--gold)" stroke-width="2"/></svg>100 % Natürlich</li>
          <li><svg viewBox="0 0 24 24"><circle cx="12" cy="12" r="10.5" fill="none" stroke="var(--gold)" stroke-width="1.5"/><path d="M7 12.5l3.2 3.2L17 9" fill="none" stroke="var(--gold)" stroke-width="2"/></svg>100 % Vegan</li>
          <li><svg viewBox="0 0 24 24"><circle cx="12" cy="12" r="10.5" fill="none" stroke="var(--gold)" stroke-width="1.5"/><path d="M7 12.5l3.2 3.2L17 9" fill="none" stroke="var(--gold)" stroke-width="2"/></svg>100 % Glutenfrei</li>
        </ul>
        <div class="bio-badge" role="img" aria-label="Bio-Siegel"></div>
        <ul class="facts">
          <li>Biozertifiziert</li>
          <li>Voller Terpeneffekt</li>
          <li>Keine Konservierungsstoffe</li>
          <li>THC &lt; 0,05 %.</li>
        </ul>
        <p class="ingredients">Inhaltsstoffe:<br>Bio Hanfsamenöl<br>(kaltgepresst)<br>Bio Hanfsamenextrakt</p>
      </div>
    </div>

    <div class="flap flap--bottom">
      <p class="batch">Charge:<br>Mindestens haltbar bis:</p>
      <div class="batch-field"></div>
    </div>

    <p class="volume">10 ml</p>
  </section>
</main>
</body>
</html>
```